2 Business Card Designs

Need two business cards designed:
1) for lumora studio (wedding video) website is lumorastudio.com.au
2) for lumora studio (corporate video) website is lumorastudio.net.au

I am looking for something simple, no fancy shapes etc. Just elegant, simple and classy.

Both companies are video companies, one specialising in weddings the other corporate videos. Neither card needs to have any pics of video or camera related images. Please use same colour schemes as respective websites.

Logo is the same but can change colour.

Industry/Entity Type

Camera

Requirements
Must have
• Logo should be either all white or a colour to match websites
Should not have
• swirls, flowers, shapes, etc.

```html
<!DOCTYPE html>
<html lang="en">
<head>
<meta charset="utf-8">
<title>lumora studio – business card</title>
<link rel="stylesheet" href="https://fonts.googleapis.com/css2?family=Tinos:ital,wght@0,400;0,700;1,700&display=swap">
<style>
  :root {
    --backdrop: #3b3b3b;
    --gold-light: #d6c57c;
    --gold-mid: #bfae68;
    --gold-dark: #978850;
    --band: #464646;
    --band-dark: #3a3a3a;
    --frame-line: rgba(80, 68, 30, 0.55);
    --name-fill: #b89c2e;
    --name-edge: #4f4006;
    --ink: #0b0b0b;
    --web-gold: #d8c57e;
  }
  * { margin: 0; padding: 0; box-sizing: border-box; }
  html, body {
    width: 1200px;
    height: 734px;
    overflow: hidden;
    background: var(--backdrop);
  }
  .business-card {
    position: absolute;
    left: 160px;
    top: 126px;
    width: 880px;
    height: 482px;
    background: radial-gradient(ellipse at 60% 45%, var(--gold-light) 0%, var(--gold-mid) 50%, var(--gold-dark) 100%);
    overflow: hidden;
  }
  .card-art {
    position: absolute;
    inset: 0;
    width: 880px;
    height: 482px;
  }
  .brand-name,
  .brand-web {
    position: absolute;
    white-space: nowrap;
    transform: translate(-50%, -50%) rotate(-53.6deg);
    font-family: "Tinos", "Times New Roman", serif;
  }
  .brand-name {
    left: 110px;
    top: 150px;
    font-size: 40px;
    font-weight: 400;
    color: var(--ink);
  }
  .brand-web {
    left: 152px;
    top: 206px;
    font-size: 17px;
    font-weight: 400;
    color: var(--web-gold);
  }
  .holder {
    position: absolute;
    left: 515px;
    top: 222px;
    transform: translate(-50%, -50%);
    text-align: center;
    font-family: "Tinos", "Times New Roman", serif;
  }
  .holder-name {
    display: block;
    font-size: 70px;
    font-weight: 700;
    font-style: italic;
    line-height: 1;
    color: var(--name-fill);
    -webkit-text-stroke: 2px var(--name-edge);
    text-shadow: 3px 4px 4px rgba(60, 45, 0, 0.55);
    white-space: nowrap;
  }
  .holder-title {
    display: block;
    margin-top: -4px;
    font-size: 26px;
    font-weight: 700;
    font-style: italic;
    letter-spacing: 1px;
    color: var(--ink);
  }
</style>
</head>
<body>
  <div class="business-card">
    <svg class="card-art" viewBox="0 0 880 482" aria-hidden="true">
      <defs>
        <linearGradient id="bandShade" x1="0" y1="0" x2="1" y2="1">
          <stop offset="0" stop-color="var(--band-dark)"/>
          <stop offset="1" stop-color="var(--band)"/>
        </linearGradient>
      </defs>
      <rect class="inner-frame" x="65.5" y="97.5" width="798" height="296" fill="none" stroke="var(--frame-line)" stroke-width="1"/>
      <polygon class="corner-band" points="0,0 355,0 0,482" fill="url(#bandShade)"/>
    </svg>

    <span class="brand-name">lumora studio</span>
    <span class="brand-web">www.lumorastudio.com.au</span>

    <div class="holder">
      <span class="holder-name">Your Name</span>
      <span class="holder-title">Job Title</span>
    </div>
  </div>
</body>
</html>
```